Insurance Firm needs Stationary and Corporate Identity

We have a logo (provided) - we need a business card, letterhead, booklet cover, Benefit & Travel card design, and brand guide.
KTR (Kestrel Trust Reinsurers) is a National (Canadian) family-run benefits firm. We've been providing alternative benefit models to small and medium sized businesses for almost 25 years! Our goal is to create long-lasting customer relationships by partnering with our clients to become their dedicated benefits division instead of just selling a product to them.

Benefit & Travel Cards: We provide the benefit card to employees to allow them to pay for drugs at their pharmacy and dental services electronically.
The travel card is for medical emergencies while travelling outside of Canada.

Brand Guide: Once the stationary is complete, the brand guide will allow us to streamline the use of our logo's and fonts for internal and external use. We will expect that this will be a paid project for our design winner after the contest closes and we will negotiate the pricetag for this at that time.

Target Market(s)

Business Owners, Entrepreneurs, HR Professionals

Industry/Entity Type

Insurance Agency

Font styles to use
Sans Serif

Requirements
Must have
• business card, letterhead, health card, travel card, booklet cover (some current samples provided)

```html
<!DOCTYPE html>
<html lang="en">
<head>
<meta charset="utf-8">
<title>Kestrel Trust Reinsurers – Stationery Set</title>
<link rel="stylesheet" href="https://fonts.googleapis.com/css2?family=Montserrat:wght@500;600&family=Lora:wght@400;600&display=swap">
<style>
  :root{
    --navy:#2c3a4e;
    --navy-deep:#1f2a38;
    --seal:#34476b;
    --red:#d8302a;
    --red-deep:#b52020;
    --grey:#8e959d;
    --slate:#56657a;
    --ink:#222;
    --paper:#ffffff;
    --sky:#8fb4e0;
    --stage:#d9d9d9;
  }
  html,body{margin:0;padding:0;overflow:hidden;}
  body{width:1200px;height:1000px;background:var(--stage);}
  .board{display:block;width:1200px;height:1000px;}
  .brand-name{font-family:"Montserrat",sans-serif;font-weight:600;}
  .brand-sub{font-family:"Montserrat",sans-serif;font-weight:500;}
  .serif{font-family:"Lora",serif;}
  .mark-text{font-family:"Montserrat",sans-serif;font-weight:600;fill:#b9bdc3;}
</style>
</head>
<body>
<svg class="board" viewBox="0 0 1200 1000" xmlns="http://www.w3.org/2000/svg">

  <!-- Business card front: contact -->
  <g class="business-card card-contact" transform="translate(41,31)">
    <rect width="357" height="205" fill="var(--navy)"/>
    <circle cx="178" cy="44" r="37" fill="var(--seal)"/>
    <text class="mark-text" x="178" y="53" font-size="26" text-anchor="middle">KTR</text>
    <polygon points="0,68 50,68 78,88 278,88 306,68 357,68 357,94 0,94" fill="var(--red)"/>
    <polygon points="0,94 78,94 78,114 0,114" fill="var(--navy-deep)"/>
    <polygon points="78,88 278,88 278,114 78,114" fill="var(--red)"/>
    <polygon points="278,94 357,94 357,114 278,114" fill="var(--navy-deep)"/>
    <text class="serif" x="160" y="161" font-size="15" fill="#fff" text-anchor="end"><tspan font-weight="600">Mara</tspan> Lindqvist</text>
    <text class="serif" x="160" y="174" font-size="10" fill="#fff" text-anchor="end">Creative Design</text>
    <line x1="179" y1="132" x2="179" y2="192" stroke="var(--red)" stroke-width="1.5"/>
    <g class="contact-icons" fill="var(--red)">
      <rect x="197" y="135" width="13" height="12" rx="1"/>
      <rect x="197" y="156" width="13" height="12" rx="1"/>
      <rect x="197" y="177" width="13" height="12" rx="1"/>
    </g>
    <path d="M200,138 q1,5 6,6 l1,-1.5 -2,-1.5 -1,1 q-2,-1 -2.5,-2.5 l1,-1 -1.5,-2z" fill="#fff"/>
    <path d="M203.5,158 a2.6,2.6 0 0 1 2.6,2.6 c0,2 -2.6,4.6 -2.6,4.6 s-2.6,-2.6 -2.6,-4.6 a2.6,2.6 0 0 1 2.6,-2.6z" fill="#fff"/>
    <rect x="200" y="180" width="7" height="6" fill="none" stroke="#fff" stroke-width="1"/>
    <text class="serif" x="227" y="145" font-size="10.5" fill="#fff" font-weight="600">555 010 0000</text>
    <text class="serif" x="227" y="166" font-size="10.5" fill="#fff" font-weight="600">Your location</text>
    <text class="serif" x="227" y="187" font-size="10.5" fill="#fff" font-weight="600">mara@ktr.com</text>
  </g>

  <!-- Travel card -->
  <g class="travel-card" transform="translate(424,118)">
    <rect width="357" height="203" fill="var(--navy)"/>
    <circle cx="179" cy="70" r="28" fill="var(--seal)"/>
    <text class="mark-text" x="179" y="77" font-size="19" text-anchor="middle">KTR</text>
    <text class="brand-name" x="179" y="115" font-size="12" fill="var(--red)" text-anchor="middle">KESTREL TRUST</text>
    <line x1="113" y1="127" x2="130" y2="127" stroke="var(--grey)"/>
    <line x1="228" y1="127" x2="245" y2="127" stroke="var(--grey)"/>
    <text class="brand-sub" x="179" y="131" font-size="10.5" fill="var(--grey)" text-anchor="middle">REINSURERS</text>
    <rect x="0" y="151" width="178" height="8" fill="var(--grey)"/>
    <rect x="0" y="159" width="178" height="44" fill="#cf3532"/>
    <rect x="178" y="151" width="179" height="52" fill="var(--red-deep)"/>
    <text class="serif" x="326" y="186" font-size="14" fill="var(--sky)" text-anchor="end" letter-spacing="2">Travel Card</text>
  </g>

  <!-- Business card back -->
  <g class="business-card card-back" transform="translate(800,31)">
    <rect width="359" height="205" fill="var(--navy)"/>
    <circle cx="179" cy="67" r="47" fill="var(--seal)"/>
    <text class="mark-text" x="179" y="78" font-size="32" text-anchor="middle">KTR</text>
    <polygon points="0,102 50,102 78,122 280,122 308,102 359,102 359,128 0,128" fill="var(--red)"/>
    <rect x="0" y="128" width="78" height="21" fill="var(--navy-deep)"/>
    <rect x="78" y="122" width="202" height="27" fill="var(--red)"/>
    <rect x="280" y="128" width="79" height="21" fill="var(--navy-deep)"/>
    <text class="brand-name" x="179" y="171" font-size="16" fill="var(--red)" text-anchor="middle">KESTREL TRUST</text>
    <line x1="103" y1="184" x2="122" y2="184" stroke="var(--grey)"/>
    <line x1="236" y1="184" x2="255" y2="184" stroke="var(--grey)"/>
    <text class="brand-sub" x="179" y="188" font-size="13" fill="var(--grey)" text-anchor="middle">REINSURERS</text>
  </g>

  <!-- Identity card -->
  <g class="identity-card" transform="translate(41,295)">
    <rect width="357" height="204" fill="var(--navy)"/>
    <circle cx="178" cy="83" r="47" fill="var(--seal)"/>
    <text class="mark-text" x="178" y="94" font-size="32" text-anchor="middle">KTR</text>
    <text class="brand-name" x="178" y="154" font-size="16" fill="var(--red)" text-anchor="middle">KESTREL TRUST</text>
    <line x1="102" y1="168" x2="122" y2="168" stroke="var(--grey)"/>
    <line x1="234" y1="168" x2="254" y2="168" stroke="var(--grey)"/>
    <text class="brand-sub" x="178" y="172" font-size="13" fill="var(--grey)" text-anchor="middle">REINSURERS</text>
    <rect x="0" y="188" width="357" height="16" fill="var(--red)"/>
    <polygon points="150,188 156,188 144,204 138,204" fill="var(--navy)"/>
    <polygon points="160,188 166,188 154,204 148,204" fill="var(--navy)"/>
    <rect x="0" y="188" width="150" height="2" fill="var(--navy-deep)"/>
  </g>

  <!-- Health card -->
  <g class="health-card" transform="translate(800,296)">
    <rect width="355" height="203" fill="var(--navy)"/>
    <circle cx="68" cy="72" r="30" fill="var(--seal)"/>
    <text class="mark-text" x="68" y="79" font-size="20" text-anchor="middle">KTR</text>
    <text class="brand-name" x="68" y="116" font-size="11" fill="var(--red)" text-anchor="middle">KESTREL TRUST</text>
    <line x1="18" y1="125" x2="30" y2="125" stroke="var(--grey)"/>
    <line x1="106" y1="125" x2="118" y2="125" stroke="var(--grey)"/>
    <text class="brand-sub" x="68" y="128" font-size="9" fill="var(--grey)" text-anchor="middle">REINSURERS</text>
    <polygon points="207,49 238,49 229,71 197,71" fill="var(--slate)"/>
    <polygon points="242,49 355,49 355,71 233,71" fill="var(--slate)"/>
    <path d="M212,55 q1,6 7,7 l1.5,-1.8 -2.4,-1.8 -1.2,1.2 q-2.4,-1.2 -3,-3 l1.2,-1.2 -1.8,-2.4z" fill="#fff"/>
    <text class="serif" x="298" y="64" font-size="12.5" fill="#fff" font-weight="600" text-anchor="middle">555 010 0000</text>
    <polygon points="182,88 213,88 204,109 172,109" fill="var(--slate)"/>
    <polygon points="217,88 355,88 355,109 208,109" fill="var(--slate)"/>
    <path d="M193,91 a3.5,3.5 0 0 1 3.5,3.5 c0,2.7 -3.5,6.2 -3.5,6.2 s-3.5,-3.5 -3.5,-6.2 a3.5,3.5 0 0 1 3.5,-3.5z" fill="#fff"/>
    <text class="serif" x="292" y="103" font-size="13" fill="#fff" font-weight="600" text-anchor="middle">Your location</text>
    <polygon points="155,126 355,126 355,154 143,154" fill="var(--slate)"/>
    <text class="serif" x="355" y="137" font-size="13" fill="#fff" letter-spacing="1" text-anchor="end"><tspan font-weight="600">Mara</tspan> Lindqvist</text>
    <text class="serif" x="355" y="149" font-size="10" fill="#fff" letter-spacing="1" text-anchor="end">Creative Design</text>
    <rect x="0" y="194" width="355" height="9" fill="var(--navy-deep)"/>
    <rect x="0" y="194" width="180" height="3" fill="var(--red)"/>
    <polygon points="188,186 355,186 355,203 172,203" fill="var(--red)"/>
    <polygon points="185,190 191,190 183,203 177,203" fill="var(--navy)"/>
    <text class="serif" x="348" y="199" font-size="10" fill="#fff" text-anchor="end" letter-spacing="1">Health Card</text>
  </g>

  <!-- Booklet cover -->
  <g class="booklet-cover" transform="translate(239,559)">
    <rect width="251" height="355" fill="var(--paper)"/>
    <rect width="251" height="7" fill="var(--red)"/>
    <g role="img" aria-label="Photograph of a modern glass office building">
      <defs>
        <linearGradient id="buildingTone" x1="0" y1="0" x2="1" y2="1">
          <stop offset="0" stop-color="#5b6aa3"/>
          <stop offset="0.5" stop-color="#7a4a5a"/>
          <stop offset="1" stop-color="#8f96a8"/>
        </linearGradient>
      </defs>
      <polygon points="120,7 251,7 251,150 95,300 60,355 0,355 0,140" fill="url(#buildingTone)"/>
    </g>
    <rect x="0" y="143" width="244" height="47" fill="var(--red)" opacity="0.82"/>
    <text class="serif" x="39" y="172" font-size="22" fill="#fff">tour title</text>
    <polygon points="60,355 251,160 251,178 86,344 251,344 251,355" fill="var(--red)"/>
    <polygon points="86,344 251,178 251,344" fill="var(--paper)"/>
    <text class="serif" x="240" y="256" font-size="16" fill="var(--ink)" text-anchor="end">yout text</text>
    <text class="serif" x="240" y="270" font-size="8.5" fill="var(--ink)" text-anchor="end">in content with a deserptoin</text>
    <text class="serif" x="240" y="283" font-size="8.5" fill="var(--ink)" text-anchor="end" letter-spacing="1">of the compenybrieffly.</text>
    <text class="serif" x="240" y="296" font-size="8.5" fill="var(--ink)" text-anchor="end" letter-spacing="1">as well as contact person</text>
    <rect x="0" y="0" width="125" height="45" fill="var(--paper)"/>
    <rect width="125" height="7" fill="var(--red)"/>
    <circle cx="21" cy="28" r="11" fill="var(--seal)"/>
    <text class="mark-text" x="21" y="31" font-size="8" text-anchor="middle">KTR</text>
    <text class="brand-name" x="38" y="27" font-size="6" fill="var(--red)">KESTREL TRUST</text>
    <text class="brand-sub" x="40" y="34" font-size="5" fill="var(--grey)">REINSURERS</text>
  </g>

  <!-- Letterhead -->
  <g class="letterhead" transform="translate(658,559)">
    <rect width="247" height="351" fill="var(--paper)"/>
    <polygon points="0,0 8,0 8,45 15,60 15,351 0,351" fill="var(--red)"/>
    <polygon points="0,0 4,0 4,351 0,351" fill="var(--red-deep)"/>
    <circle cx="37" cy="26" r="11" fill="var(--seal)"/>
    <text class="mark-text" x="37" y="29" font-size="8" text-anchor="middle">KTR</text>
    <text class="brand-name" x="17" y="44" font-size="6" fill="var(--red)">KESTREL TRUST</text>
    <text class="brand-sub" x="20" y="50" font-size="5" fill="var(--grey)">REINSURERS</text>
  </g>
</svg>
</body>
</html>
```